Website and Mobile Devices design for food related application.

We need a design that is simple yet playful. The design should be food related if possible.
This design will be on the website and the mobile platform markets we intend application to be deployed too.
This application/website is called "Pickvoro[.com]. Its a random restaurant picker for the indecisive users.
Updates
Hi all, I picked a design. Again lots of great designs were submitted but I picked one that was more in line with what I wanted.
Target Market(s)
young internet savvy users.
Industry/Entity Type
Restaurant
Look and feel
Each slider illustrates characteristics of the customer's brand and the style your logo design should communicate.

```html
<!DOCTYPE html>
<html lang="en">
<head>
<meta charset="utf-8">
<title>Pickvoro.com</title>
<link rel="stylesheet" href="https://fonts.googleapis.com/css2?family=Fredoka:wght@600&family=Arimo:wght@400&display=swap">
<style>
  :root {
    --wood-light: #a8784a;
    --wood-dark: #6e4524;
    --frame: rgba(40, 24, 10, 0.55);
    --page: #ffffff;
    --brand-orange: #ff8a00;
    --plum: #922a74;
    --tab-text: #ffd800;
    --ink: #000000;
    --field-border: #9a9a9a;
    --field-hint: #777777;
    --button-bg: #e6e6e6;
  }
  * { box-sizing: border-box; margin: 0; padding: 0; }
  html, body { width: 1200px; height: 1000px; overflow: hidden; }
  body {
    position: relative;
    font-family: "Arimo", Arial, sans-serif;
    background: linear-gradient(100deg, var(--wood-light) 0%, var(--wood-dark) 45%, var(--wood-light) 75%, var(--wood-dark) 100%);
  }
  .site-frame {
    position: absolute; left: 100px; top: 85px; width: 1000px; height: 930px;
    background: var(--frame); border-radius: 12px;
  }
  .site-page {
    position: absolute; left: 114px; top: 100px; width: 972px; height: 900px;
    background: var(--page); overflow: hidden;
  }
  .site-header { position: relative; height: 132px; }
  .brand-name {
    position: absolute; left: 34px; top: 16px;
    font-family: "Fredoka", Arial, sans-serif; font-weight: 600;
    font-size: 84px; line-height: 1; color: var(--brand-orange); letter-spacing: -1px;
  }
  .main-nav { position: absolute; left: 609px; top: 76px; display: flex; gap: 13px; }
  .nav-tab {
    display: flex; align-items: center; justify-content: center;
    width: 162px; height: 56px; border-radius: 14px 14px 0 0;
    background: var(--plum); color: var(--tab-text);
    font-family: "Fredoka", Arial, sans-serif; font-weight: 600; font-size: 27px;
    text-decoration: none;
  }
  .hero {
    position: relative; height: 610px;
    background:
      radial-gradient(ellipse at 38% 72%, #d88a2c 0%, #b5561a 35%, transparent 60%),
      radial-gradient(ellipse at 85% 40%, #5d8a2a 0%, transparent 35%),
      linear-gradient(180deg, #3a1a08 0%, #8a3a10 45%, #c98a40 100%);
  }
  .welcome-panel {
    position: absolute; left: 230px; top: 24px; width: 728px; height: 164px;
    background: rgba(255, 255, 255, 0.72); padding: 6px 12px;
  }
  .welcome-title { font-size: 44px; font-weight: 400; color: var(--plum); line-height: 50px; }
  .welcome-lead { font-size: 26px; line-height: 33px; color: var(--ink); }
  .search-row { position: absolute; left: 106px; top: 124px; display: flex; align-items: center; }
  .search-icon { width: 28px; height: 28px; margin-right: 7px; }
  .search-field {
    width: 443px; height: 30px; border: 1px solid var(--field-border); padding: 0 8px;
    font: 16px "Arimo", Arial, sans-serif; color: var(--field-hint); background: #fff;
  }
  .search-button {
    width: 127px; height: 30px; border: 1px solid var(--field-border); border-left: 0;
    background: var(--button-bg); font: 15px "Arimo", Arial, sans-serif; color: var(--ink);
  }
  .about { padding: 30px 34px 0; }
  .about-text { font-size: 16px; line-height: 19.6px; text-align: justify; color: var(--ink); }
  .about-name { font-size: 29px; color: var(--plum); margin-right: 6px; }
</style>
</head>
<body>
  <div class="site-frame"></div>
  <div class="site-page">
    <header class="site-header">
      <div class="brand-name">Pickvoro.com</div>
      <nav class="main-nav">
        <a class="nav-tab" href="#">Home</a>
        <a class="nav-tab" href="#">Contact Us</a>
      </nav>
    </header>
    <section class="hero" role="img" aria-label="Photo of a crispy chicken burger with lettuce, tomato and ketchup beside a pile of fries">
      <div class="welcome-panel">
        <h1 class="welcome-title">Welcome to Pickvoro.com</h1>
        <p class="welcome-lead">Don't know what to eat? Fill in your Zip code or address and start the process to feed your mouth!</p>
        <form class="search-row">
          <svg class="search-icon" viewBox="0 0 28 28" aria-hidden="true">
            <circle cx="11" cy="11" r="8" fill="#f4f4f4" stroke="#8a8a8a" stroke-width="2.5"/>
            <line x1="17" y1="17" x2="25" y2="25" stroke="#8a8a8a" stroke-width="4" stroke-linecap="round"/>
          </svg>
          <input class="search-field" type="text" placeholder="Location (Zip code or City e.g. 90034 or Santa Monica CA)">
          <button class="search-button" type="button">Feed my mouth!</button>
        </form>
      </div>
    </section>
    <section class="about">
      <p class="about-text"><span class="about-name">Pickvoro.com</span> is a random restaurant picker for the indecisive users. Far far away, behind the word mountains, far from the countries Vokalia and Consonantia, there live the blind texts. Separated they live in Bookmarksgrove right at the coast of the Semantics, a large language ocean. A small river named Duden flows by their place and supplies it with the necessary regelialia. It is a paradisematic country, in which roasted parts of sentences fly into your mouth. Even the all-powerful Pointing has no control about the blind texts it is an almost unorthographic life One day however a small line of blind text by the name of Lorem Ipsum decided to leave for the far World of Grammar.</p>
    </section>
  </div>
</body>
</html>
```